依頼概要
■依頼の目的/概要
弊社は和洋菓子の製造販売をしている会社です。
お得意様向けのDM作成をお願いいたします。

■依頼詳細
デザイン案:DMラフや前回DM(創業祭)を参考に制作願います。
サイズ:はがきサイズ
入稿:弊社の取引のある印刷屋さんへ入稿致します。

■要望点
おいしそうに見せて頂けると助かります。
前回イベント(創業祭)のデータを添付いたしました。参考にしてください。
「DM制作にあたって」という添付ファイルをお読みいただき、趣旨をご理解の上制作お願いいたします。

```html
<!DOCTYPE html>
<html lang="ja">
<head>
<meta charset="utf-8">
<title>翠月 白桃フェア</title>
<link href="https://fonts.googleapis.com/css2?family=M+PLUS+Rounded+1c:wght@400;700;800&family=Noto+Sans+JP:wght@400;500;700;900&display=swap" rel="stylesheet">
<style>
  :root{
    --pink:#e2357c;
    --pink-soft:#f8d3e0;
    --cream:#f7ecd6;
    --ink:#4a3a33;
    --gray:#8a7e78;
    --gold:#c9a64a;
    --white:#ffffff;
  }
  *{margin:0;padding:0;box-sizing:border-box}
  html,body{width:810px;height:1200px;overflow:hidden;background:var(--white)}
  body{font-family:"Noto Sans JP",sans-serif;color:var(--ink);position:relative}

  .photo{position:absolute}
  .photo--roll-milk{left:0;top:0;width:402px;height:350px;background:radial-gradient(ellipse at 45% 45%,#f6d9a8 0%,#efd2a6 35%,#fbeedd 70%,#fff8f0 100%)}
  .photo--roll-peach{left:408px;top:0;width:402px;height:350px;background:radial-gradient(ellipse at 85% 15%,#f4a996 0%,#f7cdb6 30%,#fbeadb 60%,#fff8f0 100%)}
  .catch{position:absolute;top:14px;font-family:"M PLUS Rounded 1c",sans-serif;font-weight:800;font-size:27px;color:var(--pink)}
  .catch--left{left:18px}
  .catch--right{left:470px}
  .item-tag{position:absolute;top:262px}
  .item-tag--left{left:232px}
  .item-tag--right{left:636px}
  .badge{display:inline-block;background:var(--pink);color:var(--white);font-size:13px;font-weight:700;padding:2px 8px;border-radius:3px}
  .item-tag__name{font-size:17px;font-weight:700;margin-top:3px}
  .item-tag__price{font-size:22px;font-weight:900;color:var(--pink);line-height:28px}
  .item-tag__price small{font-size:14px}

  .title{position:absolute;left:0;top:362px;width:810px;height:124px;border-top:4px solid var(--pink);border-bottom:4px solid var(--pink);text-align:center}
  .title__text{font-family:"M PLUS Rounded 1c",sans-serif;font-weight:800;font-size:100px;line-height:116px;color:var(--pink);letter-spacing:4px}

  .period{position:absolute;left:22px;top:500px;display:flex;align-items:center;gap:12px}
  .period__label{width:74px;height:74px;border-radius:50%;background:var(--pink);color:var(--white);font-weight:700;font-size:18px;line-height:22px;display:flex;align-items:center;justify-content:center;text-align:center}
  .period__dates{font-family:"M PLUS Rounded 1c",sans-serif;font-weight:800;color:var(--pink);font-size:62px;letter-spacing:-1px;white-space:nowrap}
  .period__dates .dow{display:inline-block;width:34px;height:34px;border-radius:50%;background:var(--pink);color:var(--white);font-size:20px;line-height:34px;text-align:center;vertical-align:middle;margin:0 2px;letter-spacing:0}
  .period__dates .tilde{font-size:44px;vertical-align:middle}
  .lead{position:absolute;left:540px;top:507px;font-size:18px;font-weight:700;line-height:34px;white-space:nowrap}
  .lead em{font-style:normal;color:var(--pink);font-size:25px}

  .limited{position:absolute;left:18px;top:584px;background:var(--pink);color:var(--white);font-weight:700;font-size:20px;padding:3px 18px;border-radius:4px}
  .products{position:absolute;left:18px;top:622px;width:774px;display:flex;gap:12px}
  .product{flex:1;position:relative;height:230px}
  .product__photo{height:230px;border-radius:4px}
  .product__photo--peach{background:radial-gradient(circle at 45% 45%,#fbe3a8 0%,#f3cd7e 40%,#fbeedd 75%,#fff6ee 100%)}
  .product__photo--cheese{background:linear-gradient(180deg,#fde3e2 0%,#f5b7ad 55%,#fff5f1 100%)}
  .product__photo--parfait{background:linear-gradient(180deg,#fff3ee 0%,#f7b9a8 50%,#f2dfc6 100%)}
  .product__info{position:absolute;right:8px;bottom:8px;text-align:right}
  .product__name{font-size:16px;font-weight:700}
  .product__price{font-size:30px;font-weight:900;color:var(--pink);line-height:36px}
  .product__price small{font-size:16px}
  .award{position:absolute;left:26px;top:798px;width:72px;height:72px;border-radius:50%;background:var(--gold)}

  .set-photo{position:absolute;left:0;top:866px;width:300px;height:224px;background:radial-gradient(ellipse at 40% 55%,#f1d4a4 0%,#e8c69a 40%,#fbeedd 80%,#fff8f0 100%)}
  .set{position:absolute;left:318px;top:874px;width:474px}
  .set__title{font-size:24px;font-weight:900;border-bottom:3px solid var(--pink);padding-bottom:4px;margin-bottom:8px;white-space:nowrap}
  .set__title em{font-style:normal;color:var(--pink)}
  .set__row{display:flex;align-items:center;font-size:18px;font-weight:700;height:34px}
  .set__row::before{content:"";border-left:11px solid var(--pink);border-top:7px solid transparent;border-bottom:7px solid transparent;margin-right:8px}
  .set__name{flex:1;white-space:nowrap}
  .set__old{font-size:16px;color:var(--gray);text-decoration:line-through;width:66px}
  .set__arrow{color:var(--pink);margin:0 6px}
  .set__new{font-size:22px;font-weight:900;color:var(--pink);width:88px;text-align:right}
  .set__note{font-size:12px;color:var(--gray);margin-top:2px}

  .footer{position:absolute;left:0;top:1096px;width:810px;height:104px;display:flex;align-items:center;padding:0 14px;gap:14px}
  .brand{display:flex;align-items:center;gap:10px;width:250px;flex:none}
  .brand__mark{width:46px;height:46px;border-radius:50%;background:var(--ink);flex:none}
  .brand__name{font-size:28px;font-weight:700;color:var(--ink);white-space:nowrap}
  .rollday{flex:1;height:92px;border:2px solid var(--pink);border-radius:8px;padding:6px 12px;display:flex;align-items:center;gap:10px}
  .rollday__body{flex:1;min-width:0}
  .rollday__head{display:flex;align-items:center;gap:10px}
  .rollday__chip{background:var(--pink);color:var(--white);font-size:13px;font-weight:700;padding:2px 8px;border-radius:3px;white-space:nowrap}
  .rollday__next{font-size:19px;font-weight:900;white-space:nowrap}
  .rollday__next em{font-style:normal;color:var(--pink);font-size:25px}
  .rollday__text{font-size:11.5px;line-height:16px;margin-top:3px}
  .rollday__photo{width:60px;height:60px;border-radius:50%;flex:none;background:radial-gradient(circle,#f6e2c2 0%,#e9c597 70%,#f7ecd6 100%)}
</style>
</head>
<body>
  <div class="photo photo--roll-milk" role="img" aria-label="白桃ミルクロールの写真"></div>
  <div class="photo photo--roll-peach" role="img" aria-label="高原桃ロールと白桃の写真"></div>
  <p class="catch catch--left">白桃と練乳のコラボ！</p>
  <p class="catch catch--right">大人気商品！</p>
  <div class="item-tag item-tag--left">
    <span class="badge">白桃フェア限定</span>
    <p class="item-tag__name">白桃ミルクロール</p>
    <p class="item-tag__price">1,400<small>円</small></p>
  </div>
  <div class="item-tag item-tag--right">
    <span class="badge">限定商品</span>
    <p class="item-tag__name">高原桃ロール</p>
    <p class="item-tag__price">1,300<small>円</small></p>
  </div>

  <div class="title"><h1 class="title__text">翠月白桃フェア</h1></div>

  <div class="period">
    <div class="period__label">開催<br>期間</div>
    <div class="period__dates">7/28<span class="dow">金</span><span class="tilde">〜</span>7/31<span class="dow">月</span></div>
  </div>
  <p class="lead">旬の桃をふんだんに使った<br><em>白桃フェア</em>を開催します！</p>

  <div class="limited">白桃フェア限定</div>
  <div class="products">
    <div class="product">
      <div class="product__photo product__photo--peach" role="img" aria-label="丸ごと白桃の焼き菓子の写真"></div>
      <div class="product__info"><p class="product__name">丸ごと白桃(桃焼)</p><p class="product__price">500<small>円</small></p></div>
    </div>
    <div class="product">
      <div class="product__photo product__photo--cheese" role="img" aria-label="白桃レアチーズの写真"></div>
      <div class="product__info"><p class="product__name">白桃レアチーズ</p><p class="product__price">450<small>円</small></p></div>
    </div>
    <div class="product">
      <div class="product__photo product__photo--parfait" role="img" aria-label="白桃パフェの写真"></div>
      <div class="product__info"><p class="product__name">白桃パフェ</p><p class="product__price">600<small>円</small></p></div>
    </div>
  </div>
  <div class="award" aria-hidden="true"></div>

  <div class="set-photo" role="img" aria-label="ロールケーキのハーフセットの写真"></div>
  <section class="set">
    <h2 class="set__title"><em>白桃フェア</em>だけのお買い得ハーフセット</h2>
    <div class="set__row"><span class="set__name">プレーン × チョコ</span><span class="set__old">1,800円</span><span class="set__arrow">▶</span><span class="set__new">1,500円</span></div>
    <div class="set__row"><span class="set__name">プレーン × マロン</span><span class="set__old">1,900円</span><span class="set__arrow">▶</span><span class="set__new">1,600円</span></div>
    <div class="set__row"><span class="set__name">プレーン × 高原桃ロール</span><span class="set__old">2,150円</span><span class="set__arrow">▶</span><span class="set__new">1,800円</span></div>
    <div class="set__row"><span class="set__name">プレーン × 白桃ミルクロール</span><span class="set__old">2,250円</span><span class="set__arrow">▶</span><span class="set__new">1,900円</span></div>
    <p class="set__note">※数量限定となります</p>
  </section>

  <footer class="footer">
    <div class="brand"><span class="brand__mark"></span><span class="brand__name">Dolce Roll</span></div>
    <div class="rollday">
      <div class="rollday__body">
        <div class="rollday__head"><span class="rollday__chip">毎月6日はロールの日</span><span class="rollday__next">次回は<em>8/6</em>(日)です！</span></div>
        <p class="rollday__text">ロールケーキお買い上げで「森の朝たまご」2コ入りパックを1パックプレゼント！<br>※お一人様1パック限りとさせていただきます。</p>
      </div>
      <div class="rollday__photo" role="img" aria-label="ロールケーキの断面写真"></div>
    </div>
  </footer>
</body>
</html>
```